Automotive Accessories Business Card

Design a business template that match our new logo design and our industry.

https://www.kelvorauto.com/

Target Market(s)

Aftermarket auto parts and accessories

Industry/Entity Type

automotive

Contact Information for Business Card

company logo

Font styles to use
Serif
Sans Serif

Colors
EB3D1F
EC4F4E
F09395
F8D3D4
FCEDEE

```html
<!DOCTYPE html>
<html lang="en">
<head>
<meta charset="utf-8">
<title>Kelvor Auto Parts – Business Card</title>
<link href="https://fonts.googleapis.com/css2?family=Montserrat:wght@400;500;700;800&display=swap" rel="stylesheet">
<style>
  :root {
    --backdrop: #e9e9e9;
    --card: #3f3f41;
    --card-deep: #1c1c1d;
    --card-grey: #8a8a8c;
    --red: #d81f26;
    --edge: #e0262d;
    --white: #ffffff;
    --soft: #dcdcdc;
  }
  * { margin: 0; padding: 0; box-sizing: border-box; }
  html, body {
    width: 1200px; height: 802px; overflow: hidden;
    background: var(--backdrop);
    font-family: "Montserrat", Arial, sans-serif;
  }
  .canvas {
    width: 1200px; height: 802px;
    display: flex; align-items: center; justify-content: center; gap: 40px;
  }
  .card {
    width: 540px; height: 309px;
    position: relative;
    border-bottom: 4px solid var(--edge);
    border-right: 2px solid var(--edge);
    box-shadow: 0 14px 30px rgba(0,0,0,.18);
    overflow: hidden;
  }
  .card--front { background: var(--card); color: var(--white); }

  .brand {
    position: absolute; left: 44px; top: 48px;
    display: flex; align-items: center; gap: 12px;
  }
  .brand__square { width: 22px; height: 22px; background: var(--red); }
  .brand__name {
    font-weight: 800; font-size: 27px; letter-spacing: 1.5px;
    text-transform: uppercase; color: var(--white);
  }

  .details {
    position: absolute; left: 44px; top: 130px;
    display: flex; align-items: center; gap: 22px;
  }
  .person { text-align: right; }
  .person__name {
    color: var(--red); font-weight: 800; font-size: 19px; letter-spacing: 2px;
    text-transform: uppercase;
  }
  .person__role { font-size: 13px; font-weight: 500; margin-top: 4px; }
  .divider { width: 1px; height: 62px; background: var(--soft); }
  .contacts { list-style: none; font-size: 13px; line-height: 22px; }
  .contacts li { display: flex; align-items: center; gap: 9px; }
  .contacts svg { width: 11px; height: 11px; fill: var(--red); flex: none; }

  .address {
    position: absolute; left: 44px; bottom: 42px;
    font-size: 14px; font-weight: 500; letter-spacing: .3px;
  }

  .card--back {
    background: linear-gradient(120deg, var(--card-deep) 0%, var(--card) 50%, var(--card-grey) 100%);
  }
  .pattern { position: absolute; inset: 0; }
  .back-brand {
    position: absolute; left: 50%; top: 50%; transform: translate(-50%, -50%);
    display: flex; align-items: center; gap: 10px;
  }
  .back-brand .brand__square { width: 16px; height: 16px; }
  .back-brand .brand__name { font-size: 21px; }
</style>
</head>
<body>
<main class="canvas">
  <section class="card card--front">
    <div class="brand">
      <span class="brand__square"></span>
      <span class="brand__name">Kelvor Auto Parts</span>
    </div>

    <div class="details">
      <div class="person">
        <p class="person__name">Marcus Hale</p>
        <p class="person__role">Manager</p>
      </div>
      <span class="divider"></span>
      <ul class="contacts">
        <li>
          <svg viewBox="0 0 24 24"><path d="M6.6 10.8a15.1 15.1 0 0 0 6.6 6.6l2.2-2.2c.3-.3.7-.4 1-.2 1.1.4 2.3.6 3.6.6.6 0 1 .4 1 1V20c0 .6-.4 1-1 1A17 17 0 0 1 3 4c0-.6.4-1 1-1h3.5c.6 0 1 .4 1 1 0 1.3.2 2.5.6 3.6.1.3 0 .7-.2 1z"/></svg>
          1-866-555-0142
        </li>
        <li>
          <svg viewBox="0 0 24 24"><path d="M2 5h20v14H2zm2 2v.5l8 5 8-5V7zm0 2.8V17h16V9.8l-8 5z"/></svg>
          sales@kelvorauto.com
        </li>
        <li>
          <svg viewBox="0 0 24 24"><path d="M12 2a10 10 0 1 0 0 20 10 10 0 0 0 0-20zm6.9 6h-3a15 15 0 0 0-1.3-3.9A8 8 0 0 1 18.9 8zM12 4c.8 1.2 1.5 2.5 1.9 4h-3.8c.4-1.5 1.1-2.8 1.9-4zM4.3 14a8 8 0 0 1 0-4h3.4a16 16 0 0 0 0 4zm.8 2h3a15 15 0 0 0 1.3 3.9A8 8 0 0 1 5.1 16zm3-8h-3a8 8 0 0 1 4.3-3.9C8.8 5.3 8.4 6.6 8.1 8zM12 20c-.8-1.2-1.5-2.5-1.9-4h3.8c-.4 1.5-1.1 2.8-1.9 4zm2.3-6H9.7a14 14 0 0 1 0-4h4.6a14 14 0 0 1 0 4zm.3 5.9c.6-1.2 1-2.5 1.3-3.9h3a8 8 0 0 1-4.3 3.9zm1.7-5.9a16 16 0 0 0 0-4h3.4a8 8 0 0 1 0 4z"/></svg>
          www.kelvorauto.com
        </li>
      </ul>
    </div>

    <p class="address">240 W. Harbor Ave. Unit B, Fairview, CA 91702</p>
  </section>

  <section class="card card--back">
    <div class="pattern" role="img" aria-label="Repeating embossed brand mark pattern fading from black to grey"></div>
    <div class="back-brand">
      <span class="brand__square"></span>
      <span class="brand__name">Kelvor Auto Parts</span>
    </div>
  </section>
</main>
</body>
</html>
```